Business Card for beauty technology startup

Design Glowmi Business Card for a Beauty, based on the website identity and colors (https://www.glowmi-example.com).
Glowmi is a beauty tech startup that gathers helpful product info for beauty lovers and consumers (such as availability on stores, price range and product reviews) for makeup products. The card design must be young, colorful but clean, and very modern.

Target Market(s)

woman, 15-35

Industry/Entity Type

Cosmetics

Contact Information for Business Card

Full Name, address, phone

Font styles to use
Other font styles liked:
• Advent Pro

Colors
e34297
86cfc6
ffffff
5c5c5c
e8e8e8
e667a6
b2b2b2

Requirements
Must have
• One full colored side with a creative design and another with card info
• Use Color palette: #95C5C5 and/or #D38AA5
• Use fonts: Advent Pro
• Use website identity: https://www.glowmi-example.com
Nice to have
• If needed extra font: Roboto

```html
<!DOCTYPE html>
<html lang="en">
<head>
<meta charset="utf-8">
<title>Glowmi Business Card</title>
<link rel="stylesheet" href="https://fonts.googleapis.com/css2?family=Advent+Pro:wght@300;400;500&display=swap">
<style>
  :root {
    --backdrop: #5b7876;
    --card-teal: #95c5c5;
    --card-teal-deep: #83b6b4;
    --card-white: #ededeb;
    --teal-ink: #6fb3b3;
    --grey-ink: #5c5c5c;
    --soft-grey: #b2b2b2;
    --white: #ffffff;
  }
  * { margin: 0; padding: 0; box-sizing: border-box; }
  html, body {
    width: 1200px; height: 900px; overflow: hidden;
    background: var(--backdrop);
    font-family: "Advent Pro", sans-serif;
  }
  .canvas { position: relative; width: 1200px; height: 900px; }

  .card { position: absolute; overflow: hidden; box-shadow: 0 6px 14px rgba(0,0,0,0.35); }

  /* Front side */
  .card-front {
    left: 154px; top: 154px; width: 340px; height: 593px;
    background: linear-gradient(180deg, #a6d3d1 0%, var(--card-teal) 45%, var(--card-teal-deep) 100%);
  }
  .front-ring {
    position: absolute; left: 44px; top: 145px; width: 248px; height: 248px;
    border: 3px solid rgba(255,255,255,0.14); border-radius: 50%;
  }
  .front-rule {
    position: absolute; left: 169px; top: 0; width: 2px; height: 46px;
    background: var(--white);
  }
  .front-url {
    position: absolute; left: 160px; top: 76px; width: 20px; height: 196px;
    writing-mode: vertical-rl; transform: rotate(180deg);
    text-align: start;
    color: var(--white); font-size: 17px; font-weight: 400; letter-spacing: 1px;
    white-space: nowrap; line-height: 20px;
  }
  .front-brand {
    position: absolute; left: 44px; top: 482px;
    display: flex; align-items: center; gap: 24px;
  }
  .brand-dot {
    width: 60px; height: 60px; border: 2px solid var(--white); border-radius: 50%;
  }
  .front-name {
    color: var(--white); font-size: 40px; font-weight: 300; letter-spacing: 5px; line-height: 1;
  }

  /* Info side */
  .card-back {
    left: 513px; top: 428px; width: 561px; height: 319px;
    background: var(--card-white);
  }
  .back-ring {
    position: absolute; left: 47px; top: 60px; width: 240px; height: 240px;
    border: 3px solid rgba(0,0,0,0.05); border-radius: 50%;
  }
  .contact {
    position: absolute; left: 348px; top: 54px;
    color: var(--grey-ink); font-size: 15px; font-weight: 400; line-height: 18px;
  }
  .contact-rule { width: 17px; height: 2px; background: var(--teal-ink); margin: 7px 0 13px; }
  .contact .accent { color: var(--teal-ink); }
  .holder {
    position: absolute; left: 44px; top: 222px;
    display: flex; align-items: center; gap: 14px;
  }
  .holder .brand-dot { width: 46px; height: 46px; border-color: var(--teal-ink); }
  .holder-name {
    color: var(--teal-ink); font-size: 23px; font-weight: 400; letter-spacing: 0.5px; line-height: 1;
  }
  .holder-role { color: var(--grey-ink); font-size: 15px; margin-top: 6px; line-height: 1; }
</style>
</head>
<body>
<div class="canvas">
  <section class="card card-front">
    <div class="front-ring"></div>
    <div class="front-rule"></div>
    <div class="front-url">www.glowmi-example.com</div>
    <div class="front-brand">
      <div class="brand-dot"></div>
      <div class="front-name">GLOWMI</div>
    </div>
  </section>

  <section class="card card-back">
    <div class="back-ring"></div>
    <div class="contact">
      <p>120 Harbor Lane</p>
      <p>Coral Bay, Florida 33300</p>
      <div class="contact-rule"></div>
      <p>555-010-2040</p>
      <p>info@glowmi-example.com</p>
      <p>www.<span class="accent">glowmi-example</span>.com</p>
    </div>
    <div class="holder">
      <div class="brand-dot"></div>
      <div>
        <p class="holder-name">MARISA VALE</p>
        <p class="holder-role">Managing Director</p>
      </div>
    </div>
  </section>
</div>
</body>
</html>
```